Logo and Business Card Design for Innovative Corporate Law Firm

Valmor Advogados is a new, young and innovative law firm focused in corporate law, mainly helping start-ups in the incorporation process, liasing with strategic investors, funds, private equity and venture/seed capital businesses around the world.

We need a logo and business card design that correctly captures our modern and savvy, yet sober, approach to legal practice.

We are looking to starting with the logo and business card designs and further ahead move on to stationery, website etc.

We are located in São Paulo/Brazil, but we expect our logo and stationery design to be able to reach and connect to possible clients worldwide due to the international characteristic of our practice.

Be creative! We have no restrictions on colors, one-sided or two-sided cards, logos, font styles...
Updates

Guys, just to be clear: The project shall contemplate a full stationery design, but the logo and business card may be proposed in advance due to our urgent need to have these cards ready for our clients. The other stationery items may be proposed later on. Many thanks!

Dear all, please be aware that the logo should look good both in collor and black and white. 

Thanks

Industry/Entity Type

Business

Requirements
Must have
• Modern but sober approach
Nice to have
• I tend to like grey collor schemes with red touches, but this is not a must have...
Should not have
• Excessively bright, shiny look, that will make our legal services look too commercial. No excesses.

```html
<!DOCTYPE html>
<html lang="pt-BR">
<head>
<meta charset="utf-8">
<title>Valmor Advogados — Business Card</title>
<link rel="stylesheet" href="https://fonts.googleapis.com/css2?family=Cormorant+Garamond:wght@500;600&family=Montserrat:wght@500;600&display=swap">
<style>
  :root {
    --bg: #e8e5e0;
    --brand-blue: #2b3fa6;
    --brand-blue-deep: #1f2f8c;
    --edge-grey: #d7d9de;
    --paper: #ffffff;
    --ink: #3a3f55;
    --ink-soft: #7a7f92;
    --watermark: #eef0f6;
    --white: #ffffff;
  }
  * { margin: 0; padding: 0; box-sizing: border-box; }
  html, body {
    width: 1200px; height: 1023px; overflow: hidden;
    background: var(--bg);
  }
  .sheet {
    width: 1200px; height: 1023px;
    display: flex; flex-direction: column; align-items: center; justify-content: center;
    gap: 70px;
  }
  .card {
    position: relative;
    width: 660px; height: 378px;
    border-radius: 4px;
    overflow: hidden;
    box-shadow: 0 10px 28px rgba(0,0,0,0.12);
  }

  /* Front */
  .card-front {
    background: linear-gradient(160deg, var(--brand-blue) 0%, var(--brand-blue-deep) 100%);
    color: var(--white);
  }
  .card-front .edge-band {
    position: absolute; top: 0; right: 0; bottom: 0; width: 44px;
    background: var(--edge-grey);
  }
  .card-front .identity {
    position: absolute; top: 0; left: 0; right: 44px; bottom: 0;
    display: flex; flex-direction: column; align-items: center; justify-content: center;
  }
  .mark-circle {
    width: 92px; height: 92px; border-radius: 50%;
    background: var(--white);
    margin-bottom: 22px;
  }
  .firm-name {
    font-family: "Cormorant Garamond", serif;
    font-weight: 500;
    font-size: 46px;
    letter-spacing: 1.5px;
    text-transform: uppercase;
    line-height: 1;
  }
  .firm-tagline {
    align-self: flex-end;
    margin-right: 92px;
    margin-top: 6px;
    font-family: "Cormorant Garamond", serif;
    font-weight: 500;
    font-size: 15px;
    letter-spacing: 5px;
    text-transform: uppercase;
  }
  .firm-web {
    margin-top: 30px;
    font-family: "Montserrat", sans-serif;
    font-weight: 600;
    font-size: 12px;
    letter-spacing: 2.5px;
    text-transform: uppercase;
  }

  /* Back */
  .card-back { background: var(--paper); color: var(--ink); }
  .card-back .edge-band {
    position: absolute; top: 0; left: 0; bottom: 0; width: 18px;
    background: var(--brand-blue);
  }
  .card-back .edge-band-grey {
    position: absolute; top: 0; left: 18px; bottom: 0; width: 26px;
    background: var(--edge-grey);
  }
  .watermark-circle {
    position: absolute; right: -60px; top: 70px;
    width: 300px; height: 300px; border-radius: 50%;
    background: var(--watermark);
  }
  .contact-list {
    position: absolute; left: 84px; top: 50%; transform: translateY(-50%);
    list-style: none;
    font-family: "Montserrat", sans-serif;
    font-weight: 500;
    font-size: 14px;
    line-height: 1.4;
  }
  .contact-item {
    display: flex; align-items: flex-start; gap: 14px;
    margin-bottom: 14px;
  }
  .contact-item:last-child { margin-bottom: 0; }
  .contact-icon { width: 16px; height: 16px; flex: none; margin-top: 2px; }
  .contact-icon * { fill: none; stroke: var(--brand-blue); stroke-width: 1.6; stroke-linecap: round; stroke-linejoin: round; }
  .contact-sub { color: var(--ink-soft); }
</style>
</head>
<body>
<main class="sheet">
  <section class="card card-front" aria-label="Business card front">
    <div class="edge-band"></div>
    <div class="identity">
      <div class="mark-circle"></div>
      <h1 class="firm-name">Valmor Advogados</h1>
      <p class="firm-tagline">Law Firm</p>
      <p class="firm-web">www.valmoradvogados.com.br</p>
    </div>
  </section>

  <section class="card card-back" aria-label="Business card back">
    <div class="edge-band"></div>
    <div class="edge-band-grey"></div>
    <div class="watermark-circle"></div>
    <ul class="contact-list">
      <li class="contact-item">
        <svg class="contact-icon" viewBox="0 0 16 16"><path d="M8 15s5-5 5-9a5 5 0 0 0-10 0c0 4 5 9 5 9z"/><circle cx="8" cy="6" r="1.8"/></svg>
        <div>Rua das Palmeiras, 450<br><span class="contact-sub">São Paulo · SP · Brasil</span></div>
      </li>
      <li class="contact-item">
        <svg class="contact-icon" viewBox="0 0 16 16"><path d="M3 1.5h3l1.2 3.2-1.8 1.2a8 8 0 0 0 4.7 4.7l1.2-1.8 3.2 1.2v3a1.5 1.5 0 0 1-1.6 1.5A12.5 12.5 0 0 1 1.5 3.1 1.5 1.5 0 0 1 3 1.5z"/></svg>
        <div>+55 11 4000 0000</div>
      </li>
      <li class="contact-item">
        <svg class="contact-icon" viewBox="0 0 16 16"><rect x="1.5" y="3" width="13" height="10" rx="1"/><path d="M1.5 4l6.5 5 6.5-5"/></svg>
        <div>contato@valmoradvogados.com.br</div>
      </li>
      <li class="contact-item">
        <svg class="contact-icon" viewBox="0 0 16 16"><circle cx="8" cy="8" r="6.5"/><path d="M1.5 8h13M8 1.5c2 2 2.8 4.2 2.8 6.5S10 12.5 8 14.5C6 12.5 5.2 10.3 5.2 8S6 3.5 8 1.5z"/></svg>
        <div>www.valmoradvogados.com.br</div>
      </li>
    </ul>
  </section>
</main>
</body>
</html>
```